New Business Card Design Project

hello again,
i have an awful year and we were not able to complete our logo plan. we would like to use our #1 logo for business card design process. the primary colors for business card should be white background with orange & black letters. our business is mobil truck cranes. we deliver heavy stuff and unload cargo with crane that is mounted on our trucks.
here is our business card info:
HARBOR LIFT HAULERS, INC.
428 WESTCOTT AVE
MERRICK, NY 11542
OFFICE - 516 487 3091
DIRECT - 1 888 LIFT HAULS
MARK@HLHAULERS.COM
PLEASE also try to get our slogan on card .... "Our Loads Keep Rollin"
lastly please also put "24 hour Knuckleboom Service"
you can call me anytime 24/7 to discuss...my cell # is: 516 759 2036
please also list: Mark Delroy, President
Target Market(s)
Heavy Construction industry
Industry/Entity Type
heavy construction industry
Contact Information for Business Card
24 Hr Knuckleboom Service

```html
<!DOCTYPE html>
<html lang="en">
<head>
<meta charset="utf-8">
<title>Harbor Lift Haulers – Business Card</title>
<link href="https://fonts.googleapis.com/css2?family=Montserrat:wght@500;600;700;800&family=Oswald:wght@600&display=swap" rel="stylesheet">
<style>
  :root {
    --backdrop: #b9bcbf;
    --card-black: #000000;
    --card-white: #ffffff;
    --orange: #f07a1e;
    --ink: #1a1a1a;
    --white: #ffffff;
    --art-dark: #3a3a3a;
    --art-light: #d8d8d8;
  }
  * { margin: 0; padding: 0; box-sizing: border-box; }
  html, body {
    width: 1187px; height: 1200px; overflow: hidden;
    background: var(--backdrop);
    font-family: "Montserrat", Arial, sans-serif;
  }
  .card { position: absolute; overflow: hidden; }
  .card-front { left: 207px; top: 114px; width: 774px; height: 446px; background: var(--card-black); }
  .card-back { left: 208px; top: 640px; width: 772px; height: 442px; background: var(--card-white); }

  .brand { position: absolute; text-align: center; }
  .brand-slogan {
    font-family: "Oswald", Arial, sans-serif; font-weight: 600;
    letter-spacing: 1px; text-transform: uppercase;
  }
  .brand-art { display: block; margin: 0 auto; border-radius: 4px; }
  .brand-name { font-weight: 800; letter-spacing: 0.5px; text-transform: uppercase; }

  .card-front .brand { left: 176px; top: 108px; width: 450px; }
  .card-front .brand-slogan { color: var(--white); font-size: 24px; }
  .card-front .brand-slogan span { color: var(--orange); }
  .card-front .brand-art { width: 390px; height: 120px; margin-top: 8px;
    background: linear-gradient(180deg, #2a2a2a, #6a6a6a); }
  .card-front .brand-name { color: var(--white); font-size: 34px; margin-top: 10px; line-height: 1; }

  .service-line {
    position: absolute; left: 0; width: 100%; top: 362px; text-align: center;
    color: var(--orange); font-weight: 800; font-size: 23px; letter-spacing: 1px;
  }

  .card-back .brand { left: 43px; top: 128px; width: 336px; }
  .card-back .brand-slogan { color: var(--ink); font-size: 18px; }
  .card-back .brand-slogan span { color: var(--orange); }
  .card-back .brand-art { width: 290px; height: 92px; margin-top: 6px;
    background: linear-gradient(180deg, var(--art-light), #9a9a9a); }
  .card-back .brand-name { color: var(--ink); font-size: 25px; margin-top: 8px; line-height: 1; }

  .contact { position: absolute; left: 426px; top: 78px; color: var(--ink); }
  .contact-name { color: var(--orange); font-weight: 700; font-size: 31px; letter-spacing: 1px; line-height: 1; }
  .contact-role { font-weight: 500; font-size: 17px; letter-spacing: 1.5px; margin-top: 6px; }
  .contact-list { list-style: none; margin-top: 20px; }
  .contact-list li { display: flex; align-items: center; gap: 8px; font-size: 18px; font-weight: 500;
    letter-spacing: 1.2px; height: 32.5px; }
  .contact-list svg { width: 14px; height: 14px; fill: var(--orange); flex: none; }
  .company { margin-top: 16px; font-size: 17px; font-weight: 500; letter-spacing: 0.8px; line-height: 22px; }
  .company-name { color: var(--orange); font-weight: 600; }

  .base-rule { position: absolute; left: 0; bottom: 0; width: 100%; height: 14px;
    background: var(--card-black); border-top: 3px solid var(--orange); }
</style>
</head>
<body>

<section class="card card-front">
  <div class="brand">
    <p class="brand-slogan">Our Loads Keep <span>"Rollin"</span></p>
    <div class="brand-art" role="img" aria-label="Illustration of a crane truck in front of a city skyline"></div>
    <p class="brand-name">Harbor Lift Haulers Inc</p>
  </div>
  <p class="service-line">24 hour Knuckleboom Service</p>
</section>

<section class="card card-back">
  <div class="brand">
    <p class="brand-slogan">Our Loads Keep <span>"Rollin"</span></p>
    <div class="brand-art" role="img" aria-label="Illustration of a crane truck in front of a city skyline"></div>
    <p class="brand-name">Harbor Lift Haulers Inc</p>
  </div>

  <div class="contact">
    <h1 class="contact-name">MARK DELROY</h1>
    <p class="contact-role">PRESIDENT</p>
    <ul class="contact-list">
      <li><svg viewBox="0 0 16 16"><path d="M3.6 1.2l2.3 2.9-1.4 1.6c.9 2.2 2.6 3.9 4.8 4.8l1.6-1.4 2.9 2.3-1.4 2.6C6.8 13.7 2.3 9.2 1 3.6z"/></svg>516 487 3091</li>
      <li><svg viewBox="0 0 16 16"><path d="M3.6 1.2l2.3 2.9-1.4 1.6c.9 2.2 2.6 3.9 4.8 4.8l1.6-1.4 2.9 2.3-1.4 2.6C6.8 13.7 2.3 9.2 1 3.6z"/></svg>1 888 LIFT HAULS</li>
      <li><svg viewBox="0 0 16 16"><path d="M1 6l7-4 7 4v8H1z M2.5 6.5L8 10l5.5-3.5" stroke="#fff" stroke-width="1"/></svg>MARK@HLHAULERS.COM</li>
      <li><svg viewBox="0 0 16 16"><circle cx="8" cy="8" r="7"/><path d="M1 8h14M8 1c-3 3-3 11 0 14M8 1c3 3 3 11 0 14" stroke="#fff" stroke-width="1" fill="none"/></svg>WWW.HLHAULERS.COM</li>
    </ul>
    <p class="company"><span class="company-name">HARBOR LIFT HAULERS, INC</span>.<br>428 WESTCOTT AVE<br>MERRICK, NY 11542</p>
  </div>

  <div class="base-rule"></div>
</section>

</body>
</html>
```